Artist needs a business card for her pencil portraits and streetscapes

My mum is an artist and does fabulous portraits and sketches with pencil and needs a business card.
She likes designs that are a bit weird or unusual. The winning design will NOT be a slick modern corporate looking logo. It should be a little bit rustic and different. Interesting patterns and textures would be great, it doesn't even need to look like a business card! Come up with something unique!

Target Market(s)

Older clientele looking for family portraits

Industry/Entity Type

Artists

Contact Information for Business Card

Basically just need the name and contact details

Font styles to use
Decorative
Script

Requirements
Must have
• Lena Dorsby
• Artist
• 0427193662
• lenadorsby@postvale.com
Nice to have
• Weird artistic backgrounds, interesting textures, unusual designs for an artistic woman.
Should not have
• Nothing ultra modern and nothing corporate looking.

```html
<!DOCTYPE html>
<html lang="en">
<head>
<meta charset="utf-8">
<title>Lena Dorsby — Artist Business Card</title>
<link href="https://fonts.googleapis.com/css2?family=Rye&family=Ubuntu&family=Fondamento&display=swap" rel="stylesheet">
<style>
  :root {
    --page: #e9e4da;
    --card-light: #3d3726;
    --card-dark: #231f15;
    --copper: #c8763a;
    --copper-deep: #9a5a26;
    --ink: #0b0a08;
  }
  html, body {
    margin: 0;
    width: 1200px;
    height: 1200px;
    overflow: hidden;
    background: var(--page);
  }
  .canvas {
    position: relative;
    width: 1200px;
    height: 1200px;
  }
  .card {
    position: absolute;
    left: 276px;
    width: 648px;
    height: 400px;
    border-radius: 32px;
    overflow: hidden;
  }
  .card--front { top: 186px; }
  .card--back { top: 614px; }
  .card__texture {
    position: absolute;
    inset: 0;
    background: radial-gradient(ellipse at 40% 35%, var(--card-light), var(--card-dark) 85%);
  }
  .outlined {
    color: var(--copper);
    -webkit-text-stroke: 8px var(--ink);
    paint-order: stroke fill;
  }
  .front__first {
    position: absolute;
    left: 40px;
    top: 62px;
    margin: 0;
    font: 112px/1 "Rye", serif;
    transform: rotate(-4deg);
    transform-origin: left bottom;
  }
  .front__last {
    position: absolute;
    left: 148px;
    top: 172px;
    font: 46px/1 "Rye", serif;
    transform: rotate(-5deg);
  }
  .front__role {
    position: absolute;
    left: 62px;
    top: 250px;
    width: 250px;
    height: 68px;
    border-radius: 34px;
    background: var(--ink);
    transform: rotate(-5deg);
    display: flex;
    align-items: center;
    justify-content: center;
    font: 40px/1 "Rye", serif;
    color: var(--copper);
  }
  .front__contact {
    position: absolute;
    left: 364px;
    top: 246px;
    padding-left: 20px;
    border-left: 8px solid var(--copper);
    font: 19px/1.75 "Ubuntu", sans-serif;
    color: var(--copper);
  }
  .dots {
    position: absolute;
    height: 0;
    border-top: 5px dotted var(--copper);
  }
  .dots--top { left: 18px; right: 20px; top: 68px; }
  .dots--left { left: 18px; width: 200px; top: 216px; }
  .dots--right { right: 20px; width: 200px; top: 216px; }
  .back__name {
    position: absolute;
    left: 0; right: 0;
    top: 88px;
    margin: 0;
    text-align: center;
    font: 74px/1 "Rye", serif;
  }
  .back__role {
    position: absolute;
    left: 0; right: 0;
    top: 192px;
    text-align: center;
    font: 46px/1 "Rye", serif;
  }
  .back__phone,
  .back__email {
    position: absolute;
    left: 0; right: 0;
    text-align: center;
    color: var(--copper-deep);
    -webkit-text-stroke: 4px var(--ink);
    paint-order: stroke fill;
  }
  .back__phone { top: 276px; font: 34px/1 "Rye", serif; }
  .back__email { top: 320px; font: 32px/1 "Fondamento", cursive; }
</style>
</head>
<body>
<main class="canvas">
  <section class="card card--front">
    <div class="card__texture" role="img" aria-label="Dark embossed paisley leather pattern"></div>
    <h1 class="front__first outlined">LENA</h1>
    <div class="front__last outlined">DORSBY</div>
    <div class="front__role">ARTIST</div>
    <div class="front__contact">
      <div>Voice&nbsp; 0427193662</div>
      <div>lenadorsby@postvale.com</div>
    </div>
  </section>

  <section class="card card--back">
    <div class="card__texture" role="img" aria-label="Dark embossed paisley leather pattern"></div>
    <div class="dots dots--top"></div>
    <h2 class="back__name outlined">LENA DORSBY</h2>
    <div class="dots dots--left"></div>
    <div class="back__role outlined">ARTIST</div>
    <div class="dots dots--right"></div>
    <div class="back__phone">0427193662</div>
    <div class="back__email">lenadorsby@postvale.com</div>
  </section>
</main>
</body>
</html>
```